For Creative Minds: A Simple Clean Book Cover that Stands Out

This will be a christian book teaching christians about divine healing. It is part of a series called "Morning Step Collection". I want the book cover to communicate the idea of healing, and specifically heavenly healing from God. These are some of the specifications below

1. General
Book to be published on print harbor platform
Dimensions: 6 x 9 inches, Paperback
Number of words: Estimated to be about 60,000 words.
Please use Indesign for design and submit the final Indesign source files along with the final design.

2. Cover image.
Image can be either human or any object that can communicate the idea above. No human faces to show up prominently.
High quality image is highly solicited.

3. Title:
" Forty Evenings Toward Lasting Renewal Within Your Soul"

3. Author name
Preferably should appear below. Open to creative ideas with titles that are better placed above.

Author's Name: Duncan Ferrow

3. Layout
Should not be too busy.
Simple and clean layout appeals more to me.

4. Series name
AS noted above, this book will be part of a series called " Morning Step Collection". I want this series name to appear somewhere in the cover and to have a simple but unique design that will be used for all subsequent titles. The Title of the book should have the emphasis.

I have attached a sample cover for one of my monthly devotional books which I choose from a contest.

ABOUT THE AUTHOR
Duncan Ferrow represents the blessed combination of Physician and Minister, bringing healing not only to the physical body but to the spiritual heart. He currently works as the Director of the Hospital Medicine Program at the Bellhaven County Care Campus in Iowa, USA. He is the Founder of Lantern & Vine Fellowship, a teaching ministry that seeks to bring believers into the fullness of grace — the glory of God — through conferences, seminars and books.

One of his notable quotes is “The Word of God is the most potent and efficient remedy for all the ailments of humanity.” This clearly portrays his experience with the Word as a Physician who is familiar with the powers, both natural and supernatural, to mend broken human beings. 

He currently lives in Iowa, USA with his wife, Lu Tessin, and daughter, Rosalind. You can reach out to Patrick using the contact information listed below.

BLURB
As a Physician and Minister, I have seen the power of modern medicine to bring about healing in the body and mind as well as the operation of the power of God to produce amazing medical results. However, many people are just not aware of the reality of divine healing. To some, it is a myth, belief or some "faith talk" in the heart. Medical miracles are real and we should take full advantage of it. As much as a love being a physician and treat patients in the hospital, I have come to see both its amazing successes and many limitations.

Industry/Entity Type

Christian

Font styles to use
Serif

Colors

Designer to choose colors to be used in the design.

Requirements
Should not have
• Too stylistic fonts

```html
<!DOCTYPE html>
<html lang="en">
<head>
<meta charset="utf-8">
<title>Forty Evenings Toward Lasting Renewal Within Your Soul — Book Cover</title>
<link href="https://fonts.googleapis.com/css2?family=Noto+Serif:ital,wght@0,700;1,700&family=Cinzel:wght@500&display=swap" rel="stylesheet">
<style>
  :root {
    --page-bg: #e4ecf2;
    --sky-top: #1a8bd6;
    --sky-mid: #6cc0ec;
    --sky-low: #b9e2f6;
    --sky-base: #c4e8f8;
    --ink: #2b2b2b;
    --accent-blue: #1f8fd0;
    --white: #ffffff;
  }
  * { margin: 0; padding: 0; box-sizing: border-box; }
  html, body {
    width: 1200px;
    height: 900px;
    overflow: hidden;
    background: var(--page-bg);
  }
  .canvas {
    position: relative;
    width: 1200px;
    height: 900px;
  }
  .book-cover {
    position: absolute;
    left: 310px;
    top: 15px;
    width: 580px;
    height: 870px;
    overflow: hidden;
    background: linear-gradient(to bottom, var(--sky-top) 0%, var(--sky-mid) 22%, var(--sky-low) 60%, var(--sky-base) 100%);
    box-shadow: 0 10px 30px rgba(40, 70, 100, 0.25);
  }
  .sky-artwork {
    position: absolute;
    left: 0;
    top: 0;
    width: 100%;
    height: 56%;
    background:
      radial-gradient(ellipse 42% 30% at 50% 34%, rgba(255,255,255,0.95) 0%, rgba(255,255,255,0.55) 35%, rgba(255,255,255,0) 75%),
      linear-gradient(to bottom, rgba(255,255,255,0) 30%, rgba(255,255,255,0.75) 62%, rgba(255,255,255,0.35) 85%, rgba(255,255,255,0) 100%);
  }
  .series-mark {
    position: absolute;
    top: 22px;
    right: 20px;
    display: flex;
    align-items: center;
    gap: 8px;
    font-family: "Noto Serif", serif;
    font-weight: 700;
    font-size: 13px;
    letter-spacing: 0.04em;
    color: var(--white);
    text-transform: uppercase;
  }
  .series-square {
    width: 14px;
    height: 14px;
    border: 2px solid var(--white);
  }
  .title-block {
    position: absolute;
    left: 0;
    top: 210px;
    width: 100%;
    text-align: center;
    font-family: "Noto Serif", serif;
    font-weight: 700;
    color: var(--ink);
  }
  .title-number {
    display: block;
    font-size: 156px;
    line-height: 0.95;
    letter-spacing: -0.01em;
  }
  .title-word {
    display: block;
    font-size: 80px;
    line-height: 1;
    margin-top: 8px;
    letter-spacing: 0.01em;
  }
  .title-phrase {
    display: block;
    font-style: italic;
    font-size: 40px;
    line-height: 1.05;
    margin-top: 12px;
  }
  .title-emphasis {
    display: block;
    font-size: 128px;
    line-height: 1;
    margin-top: 14px;
    color: var(--accent-blue);
    letter-spacing: 0.02em;
  }
  .author {
    position: absolute;
    left: 0;
    bottom: 26px;
    width: 100%;
    text-align: center;
    font-family: "Cinzel", serif;
    font-weight: 500;
    font-size: 24px;
    letter-spacing: 0.12em;
    color: var(--ink);
  }
</style>
</head>
<body>
  <main class="canvas">
    <section class="book-cover">
      <div class="sky-artwork" role="img" aria-label="Bright blue sky with white clouds, sun rays bursting from behind the clouds and a few birds in flight"></div>

      <div class="series-mark">
        <span class="series-square"></span>
        <span class="series-name">Morning Step Collection</span>
      </div>

      <h1 class="title-block">
        <span class="title-number">Forty</span>
        <span class="title-word">EVENINGS</span>
        <span class="title-phrase">toward lasting renewal<br>within your</span>
        <span class="title-emphasis">SOUL</span>
      </h1>

      <p class="author">DUNCAN FERROW, M.D.</p>
    </section>
  </main>
</body>
</html>
```